Corvantis websites redesign

Www.cor-vantis.com needs to be redesigned along with updations. The incremental material will be provided for the updations. We are looking for complete redesign of the pages with the new content. The complete write up will be provided soon

Target Market(s)

Global

Coding

Coded - Design and coding required

Number of Pages Required

5+ page

Requirements
Must have
• A clean and slick design for the Consulting.
Should not have
• Too many pictures which reduces the speed of the site

```html
<!DOCTYPE html>
<html lang="en">
<head>
<meta charset="utf-8">
<title>Corvantis – Home</title>
<link href="https://fonts.googleapis.com/css2?family=Open+Sans:wght@400;600;700&family=Roboto+Condensed:wght@400;700&display=swap" rel="stylesheet">
<style>
:root{
  --blue:#0a8fd6;
  --navy:#1c2842;
  --maroon:#4c1a1c;
  --text:#666a70;
  --grey-panel:#e3e4e7;
  --input:#ececec;
  --white:#ffffff;
}
*{box-sizing:border-box;margin:0;padding:0}
html,body{width:823px;height:1200px;overflow:hidden;background:var(--white)}
body{position:relative;font-family:"Open Sans",sans-serif;color:var(--text)}
.hero{position:absolute;left:0;top:0;width:823px;height:370px;
  background:linear-gradient(180deg,#b9cbe0 0%,#d7dde3 28%,#9a9892 55%,#6f6a62 78%,#57524c 100%);}
.hero::after{content:"";position:absolute;right:0;top:0;width:260px;height:260px;
  background:radial-gradient(circle at 90% 10%,rgba(255,246,214,.9),rgba(255,240,200,0) 70%)}
.brand{position:absolute;left:0;right:0;top:118px;display:flex;justify-content:center;align-items:center;gap:14px;z-index:1}
.brand-dot{width:56px;height:56px;border-radius:50%;background:var(--navy)}
.brand-name{font-family:"Open Sans",sans-serif;font-weight:600;font-size:48px;color:var(--navy)}
.nav{position:absolute;left:0;top:370px;width:823px;height:48px;background:var(--blue);border-bottom:4px solid var(--navy)}
.nav ul{list-style:none;display:flex;margin-left:53px;height:44px}
.nav li{font-family:"Roboto Condensed",sans-serif;font-size:14.5px;color:var(--white);line-height:44px;padding:0 23px}
.nav li.active{background:var(--navy);padding:0 24px}
.nav-pointer{position:absolute;left:403px;top:44px;width:0;height:0;border-left:8px solid transparent;border-right:8px solid transparent;border-top:7px solid var(--navy)}
.welcome-title{position:absolute;top:446px;width:823px;text-align:center;font-family:"Roboto Condensed",sans-serif;font-weight:400;font-size:29px;color:var(--maroon)}
.welcome-title span{color:var(--blue)}
.intro{position:absolute;left:108px;top:505px;width:607px;text-align:center;font-size:11px;line-height:17.5px}
.service{position:absolute;top:583px;text-align:center}
.service .icon{width:86px;height:86px;border-radius:50%;background:var(--navy);margin:0 auto;display:flex;align-items:center;justify-content:center}
.service h2{font-family:"Roboto Condensed",sans-serif;font-weight:400;font-size:18px;color:var(--blue);margin-top:19px}
.service p{font-size:10.8px;line-height:17.2px;margin-top:6px;letter-spacing:-0.1px}
.service.plain{left:52px;width:334px}
.service.structured{left:428px;width:346px}
.call{position:absolute;left:53px;top:815px;width:717px;height:99px;background:var(--grey-panel);border:1px solid #cfd0d3}
.call-dark{position:absolute;left:-1px;top:-1px;width:359px;height:99px;background:var(--navy);
  clip-path:polygon(0 0,337px 0,359px 50%,337px 100%,0 100%);display:flex;align-items:center;padding-left:20px;color:var(--white)}
.call-label{font-family:"Roboto Condensed",sans-serif;font-size:21px;margin-right:13px}
.call-phone-ring{width:43px;height:43px;border:2px solid var(--white);border-radius:50%;display:flex;align-items:center;justify-content:center;margin-right:11px}
.call-number{font-family:"Roboto Condensed",sans-serif;font-weight:700;font-size:21px}
.call-info{position:absolute;left:382px;top:20px;width:300px;font-size:11px;line-height:17px}
.call-mail{display:flex;align-items:center;gap:7px;margin-top:6px;font-size:15px;color:var(--navy)}
.newsletter-title{position:absolute;top:947px;width:823px;text-align:center;font-family:"Roboto Condensed",sans-serif;font-weight:400;font-size:29px;color:var(--blue)}
.newsletter-text{position:absolute;left:170px;top:985px;width:483px;text-align:center;font-size:11px;line-height:17px}
.field{position:absolute;top:1031px;height:29px;width:215px;background:var(--input);border:1px solid #cfcfcf;font-size:11px;color:#777;padding:7px 7px}
.field.name{left:128px}
.field.email{left:364px}
.subscribe{position:absolute;left:600px;top:1031px;width:95px;height:29px;background:var(--maroon);color:var(--white);font-family:"Roboto Condensed",sans-serif;font-size:15px;text-align:center;line-height:29px}
.footer{position:absolute;left:0;top:1100px;width:823px;height:100px;background:var(--navy)}
.social{position:absolute;top:16px;left:0;width:823px;display:flex;justify-content:center;gap:15px}
.social span{width:39px;height:39px;border-radius:50%;background:var(--white)}
.social span.first{background:var(--blue)}
.copyright{position:absolute;top:67px;width:823px;text-align:center;font-size:11px;color:var(--white)}
.copyright b{color:var(--blue);font-weight:700}
</style>
</head>
<body>
<header class="hero" role="img" aria-label="Sunlit city skyline of high-rise towers">
  <div class="brand"><span class="brand-dot"></span><span class="brand-name">Corvantis</span></div>
</header>

<nav class="nav">
  <ul>
    <li class="active">HOME</li><li>FOUNDER</li><li>CONSULTANCY</li><li>SYSTEM</li><li>CASE STUDIES</li><li>CONTACT</li>
  </ul>
  <span class="nav-pointer"></span>
</nav>

<h1 class="welcome-title">WELCOME TO <span>CORVANTIS</span></h1>
<p class="intro">Corvantis Consultancy Limited capitalizes on synergies arising from trade and investment linkages between countries and knowledge of traditional and non-traditional pools of liquidity to provide consultancy services to Emerging country banks, Corporates and SMEs.</p>

<section class="service plain">
  <div class="icon">
    <svg width="46" height="46" viewBox="0 0 46 46" fill="none" stroke="#fff" stroke-width="4.5" stroke-linecap="round">
      <path d="M38 17 A16 16 0 0 0 9 14"/>
      <path d="M8 29 A16 16 0 0 0 37 32"/>
      <path d="M39 8 L38 17 L29 16" stroke-linejoin="round"/>
      <path d="M7 38 L8 29 L17 30" stroke-linejoin="round"/>
    </svg>
  </div>
  <h2>PLAIN VANILLA FINANCING SOLUTIONS</h2>
  <p>The Consultancy provides access to local/regional banks across Hong Kong, Singapore, Dubai , New York and London and helps corporate clients in diversifying their financial partners and adding new banks to their bank group.</p>
</section>

<section class="service structured">
  <div class="icon">
    <svg width="52" height="46" viewBox="0 0 52 46" fill="#fff">
      <rect x="19" y="0" width="14" height="12" rx="2"/><rect x="24" y="12" width="4" height="8"/>
      <rect x="7" y="19" width="38" height="4"/><rect x="7" y="19" width="4" height="10"/><rect x="41" y="19" width="4" height="10"/><rect x="24" y="19" width="4" height="10"/>
      <rect x="1" y="29" width="15" height="14" rx="2"/><rect x="19" y="29" width="14" height="14" rx="2"/><rect x="36" y="29" width="15" height="14" rx="2"/>
    </svg>
  </div>
  <h2>STRUCTURED FINANCING SOLUTIONS</h2>
  <p>The Consultancy provides end-to-end structured solutions on the Payables, Receivables or Inventory side for working capital requirements with off/part/on recourse balance sheet structures. We also specialize in providing credit enhancements...</p>
</section>

<section class="call">
  <div class="call-dark">
    <span class="call-label">CALL US ON</span>
    <span class="call-phone-ring">
      <svg width="22" height="22" viewBox="0 0 24 24" fill="#fff"><path d="M6.6 10.8a15 15 0 0 0 6.6 6.6l2.2-2.2c.3-.3.7-.4 1-.2 1.1.4 2.3.6 3.6.6.6 0 1 .4 1 1V20c0 .6-.4 1-1 1A17 17 0 0 1 3 4c0-.6.4-1 1-1h3.5c.6 0 1 .4 1 1 0 1.3.2 2.5.6 3.6.1.3 0 .7-.2 1z"/></svg>
    </span>
    <span class="call-number">+852-27315096</span>
  </div>
  <div class="call-info">
    <p>Lorem Ipsum is simply dummy text of the printing and typesetting industry. Lorem Ipsum has been the industry.</p>
    <p class="call-mail">
      <svg width="18" height="14" viewBox="0 0 18 14" fill="none" stroke="#1c2842" stroke-width="1.6"><rect x="1" y="1" width="16" height="12" rx="1.5"/><path d="M1.5 2l7.5 6 7.5-6"/></svg>
      Query@cor-vantis.com
    </p>
  </div>
</section>

<h2 class="newsletter-title">NEWSLETTER</h2>
<p class="newsletter-text">Lorem Ipsum is simply dummy text of the printing and typesetting industry. Lorem Ipsum has been the industry.</p>
<div class="field name">Enter Name</div>
<div class="field email">Enter Email</div>
<div class="subscribe">SUBSCRIBE</div>

<footer class="footer">
  <div class="social"><span class="first"></span><span></span><span></span></div>
  <p class="copyright">© <b>Corvantis</b> -  2016. All Rights Reserved</p>
</footer>
</body>
</html>
```